Flyer-Design
Sehr flexibel bei Änderungswünschen. Herzlichen Dank. Würde jederzeit wieder mit Ursula zusammenarbeiten.
Zielgruppe
Wir sind eine eine Praxis und unsere Zielgruppe sind Kunden. Es sollte einen Faltflyer geben, welcher Doppelseitig bedruckt wird.
Aufgabenstellung
Ich habe genaue Vorstellungen, wie dieser Flyer aussehen soll. Jedoch bin ich auch auf neue Ideen gespannt :). Wunschvorstellung wäre ein Falzflyer (siehe Bild Musterfyler). Des weiteren habe ich ein Word gemacht, mit dem gesamten Inhalt des Textes und wie der Flyer am Besten aufgebaut werden sollte. (siehe Flyer Tierversicherung).
Die beiden letzten Abschnitte (Tipp an unsere Kunden, Fazit) sollten ein wenig auffallen. Müssen auch nicht am Schluss sein.
Des weiteren wäre ich dankbar, wenn das CI/CD der Unternehmung berücksichtig wird. Bitte werfen Sie einen Blick auf die Webseite www.felbor-tieraerzte.ch. Ein Logo ist ebenfalls im Anhang. Bei Fragen bitte melden.
Ich freue mich auf Vorschläge.

```html
<!DOCTYPE html>
<html lang="de">
<head>
<meta charset="utf-8">
<title>Tierversicherung – Glossar</title>
<link href="https://fonts.googleapis.com/css2?family=Fira+Sans:ital,wght@0,300;0,600;0,700;1,600&display=swap" rel="stylesheet">
<style>
  :root{
    --brand-red:#d5003c;
    --brand-grey:#a5a5a7;
    --rule-grey:#b9b9bb;
    --paper:#ffffff;
  }
  html,body{margin:0;padding:0;overflow:hidden;}
  body{width:1200px;height:848px;background:var(--paper);position:relative;
       font-family:"Fira Sans",Arial,sans-serif;color:var(--brand-red);}
  .top-band{position:absolute;left:0;top:0;width:1200px;height:42px;background:var(--brand-grey);}
  .section{position:absolute;width:374px;}
  .letter{position:relative;font-weight:700;font-size:18px;line-height:20px;color:var(--brand-grey);margin:0 0 3px 4px;}
  .letter svg{position:absolute;left:-23px;top:8px;}
  .entry{margin:0 0 17px 0;}
  .entry h3{margin:0;font-size:13.6px;font-weight:600;line-height:17px;}
  .entry p{margin:0;font-size:13px;font-weight:300;line-height:17.1px;}
  .entry p + p{margin-top:17px;}
  .divider{position:absolute;height:1px;width:373px;background:var(--rule-grey);}
  .col-1{left:28px;} .col-2{left:421px;} .col-3{left:814px;}
  .fazit{position:absolute;left:800px;top:679px;width:400px;height:169px;background:var(--brand-grey);color:#fff;}
  .fazit-ticks{height:7px;background:repeating-linear-gradient(90deg,#fff 0 2px,transparent 2px 5px);
               margin-top:0;border-bottom:2px solid var(--paper);}
  .fazit h2{margin:3px 0 0 14px;font-size:29px;font-weight:700;line-height:34px;}
  .fazit p{margin:2px 0 0 32px;font-size:15.6px;font-style:italic;font-weight:600;line-height:20.5px;}
</style>
</head>
<body>
<div class="top-band"></div>

<!-- Spalte 1 -->
<section class="section col-1" style="top:63px">
  <div class="letter"><svg width="8" height="4"><circle cx="2" cy="2" r="1.5" fill="none" stroke="#a5a5a7" stroke-width=".8"/><circle cx="6" cy="2" r="1.5" fill="none" stroke="#a5a5a7" stroke-width=".8"/></svg>A</div>
  <div class="entry"><h3>Abschluss</h3><p>Beim Abschluss einer Versicherung muss das Tier jung und gesund sein.</p></div>
  <div class="entry"><h3>Anbieter</h3><p>Auf dem Schweizer Markt gibt verschiedene Anbieter von Tierversicherungen wie beispielsweise Animara, Equona, Wuff-Miau, Mobilis, Alpentia und Generosa.</p><p>Wir empfehlen keinen konkreten Anbieter, da es viele verschiedene unterschiedliche Produkte auf dem Markt gibt und jeder Kunde andere Wünsche und ein anderes Budget hat. Unseres Erachtens liegen die Unterschiede im Detail.</p></div>
  <div class="entry"><h3>Altersbegrenzung</h3><p>Die Anbieter von Tierversicherungen haben Altersbegrenzungen, üblicherweise betragen diese fünf Jahre bei Katzen und sechs Jahre bei Hunden.</p></div>
  <div class="entry"><h3>Arztwahl</h3><p>Gewisse Versicherungen erlauben keine freie Tierarztwahl. Sichern Sie sich bei Vertragsabschluss ab und fragen sie explizit nach.</p></div>
  <div class="entry"><h3>Aufnahmealter</h3><p>Die Versicherungsanbieter nehmen die Tiere in der Regel im Alter von 3 Monaten auf. Wir empfehlen die Tiere so früh wie möglich zu versichern.</p></div>
  <div class="entry"><h3>Ausschlüsse</h3><p>Beachten sie, ob Ausschlüsse aus einer Versicherungsleistung existieren und ob diese für sie von Bedeutung sind.</p></div>
</section>
<div class="divider" style="left:28px;top:646px"></div>
<section class="section col-1" style="top:652px">
  <div class="letter"><svg width="8" height="4"><circle cx="2" cy="2" r="1.5" fill="none" stroke="#a5a5a7" stroke-width=".8"/><circle cx="6" cy="2" r="1.5" fill="none" stroke="#a5a5a7" stroke-width=".8"/></svg>G</div>
  <div class="entry"><h3>Geburtskrankheiten/Erbkrankheiten</h3><p>Diese werden bei vielen Angeboten ausgeschlossen oder müssen explizit dazu versichert werden.</p></div>
</section>
<div class="divider" style="left:28px;top:734px"></div>
<section class="section col-1" style="top:743px">
  <div class="letter"><svg width="8" height="4"><circle cx="2" cy="2" r="1.5" fill="none" stroke="#a5a5a7" stroke-width=".8"/><circle cx="6" cy="2" r="1.5" fill="none" stroke="#a5a5a7" stroke-width=".8"/></svg>I</div>
  <div class="entry"><h3>Impfungen</h3><p>Nur wenige Anbieter übernehmen auch Impfungen. Fall ein Anbieter diese Leistung übernimmt, hat er in der Regel einen maximalen Betrag festgelegt.</p></div>
</section>

<!-- Spalte 2 -->
<section class="section col-2" style="top:63px">
  <div class="letter"><svg width="8" height="4"><circle cx="2" cy="2" r="1.5" fill="none" stroke="#a5a5a7" stroke-width=".8"/><circle cx="6" cy="2" r="1.5" fill="none" stroke="#a5a5a7" stroke-width=".8"/></svg>K</div>
  <div class="entry"><h3>Karenzfrist</h3><p>Bei Versicherungen besteht jeweils eine Wartezeit, die zwischen Unterzeichnung der Police und einem Deckungsanspruch eingehalten werden muss. In der Regel beträgt diese für nicht-chronische Krankheiten einen Monat und bei chronischen Krankheiten drei Monate. Bei einem Unfall gibt es in der Regel keine Karenzfrist oder je nach Anbieter bis zu einem Monat.</p></div>
</section>
<div class="divider" style="left:421px;top:222px"></div>
<section class="section col-2" style="top:229px">
  <div class="letter"><svg width="8" height="4"><circle cx="2" cy="2" r="1.5" fill="none" stroke="#a5a5a7" stroke-width=".8"/><circle cx="6" cy="2" r="1.5" fill="none" stroke="#a5a5a7" stroke-width=".8"/></svg>L</div>
  <div class="entry"><h3>Leistungen</h3><p>Die inkludierten Leistungen und die gebotene Abdeckung ist genau zu prüfen. Übernimmt der Versicherungsanbieter alle Behandlungen oder sind zum Beispiel chronische Krankheiten oder Erbkrankheiten ausgeschlossen. Ein Blick auf das Kleingedruckte beim Versicherungsangebot lohnt sich.</p><p>Sie können ihr Tier entweder gegen Krankheit oder gegen Unfall oder gegen beides versichern, letzteres empfehlen wir Ihnen.</p></div>
</section>
<div class="divider" style="left:421px;top:424px"></div>
<section class="section col-2" style="top:431px">
  <div class="letter"><svg width="8" height="4"><circle cx="2" cy="2" r="1.5" fill="none" stroke="#a5a5a7" stroke-width=".8"/><circle cx="6" cy="2" r="1.5" fill="none" stroke="#a5a5a7" stroke-width=".8"/></svg>P</div>
  <div class="entry"><h3>Prämien</h3><p>Die Prämien der einzelnen Anbieter fallen unterschiedlich aus, deshalb ist es wichtig Versicherungsangebote zu vergleichen, um den passenden Tarif für ihr Haustier zu finden.</p></div>
  <div class="entry"><h3>Prämienerhöhung</h3><p>Es gibt Versicherungen, die während der Laufzeit die Prämien erhöhen, andere bieten einen Pauschalbetrag an, damit Planungssicherheit geboten wird.</p></div>
  <div class="entry"><h3>Preis</h3><p>Langfristig ist billigste Vertragsoption oft nicht die beste, da einige Versicherungen mit einem günstigeren Preis starten und im Laufe der Jahre, wenn das Tier älter wird, den Tarif erhöht.</p></div>
</section>
<div class="divider" style="left:421px;top:705px"></div>
<section class="section col-2" style="top:713px">
  <div class="letter"><svg width="8" height="4"><circle cx="2" cy="2" r="1.5" fill="none" stroke="#a5a5a7" stroke-width=".8"/><circle cx="6" cy="2" r="1.5" fill="none" stroke="#a5a5a7" stroke-width=".8"/></svg>R</div>
  <div class="entry"><h3>Rabatte</h3><p>Vereinzelte Versicherungsanbieter gewähren Rabatte, wenn in einem Versicherungsjahr keine Leistungen bezogen wurden</p></div>
</section>

<!-- Spalte 3 -->
<section class="section col-3" style="top:85px">
  <div class="entry"><h3>Rechnungsstellung</h3><p>Die erbrachten Leistungen durch den Tierarzt sind direkt vom Tierhalter zu bezahlen. Anschliessend kann die Rechnung beim Versicherungsanbieter eingereicht werden.</p></div>
</section>
<div class="divider" style="left:814px;top:165px"></div>
<section class="section col-3" style="top:170px">
  <div class="letter"><svg width="8" height="4"><circle cx="2" cy="2" r="1.5" fill="none" stroke="#a5a5a7" stroke-width=".8"/><circle cx="6" cy="2" r="1.5" fill="none" stroke="#a5a5a7" stroke-width=".8"/></svg>S</div>
  <div class="entry"><h3>Schadenfall</h3><p>Wenn ein Schadensfall eintritt, direkt den Tierarzt aufsuchen und erst anschliessend den Fall bei der Versicherung melden und gleich die Kostenübernahme abklären. Die Rechnungskopie wird bei Behandlungsabschluss der Versicherung zu Prüfung und Begleichung weitergeleitet.</p></div>
  <div class="entry"><h3>Selbstbehalt</h3><p>Der Selbstbehalt gibt an, welche Kosten bei einem Versiche­rungsfall selbst zu tragen sind. Einige Anbieter bieten ebenfalls die Option mit CHF 0 an. Falls man bei der Prämie etwas sparen möchte, sollte der Selbstbehalt auf einen höheren Betrag festgelegt werden. Einige Versicherungsanbieter ziehen den Selbstbehalt bei jedem Krankheitsfall an und andere jährlich.</p></div>
</section>
<div class="divider" style="left:814px;top:447px"></div>
<section class="section col-3" style="top:452px">
  <div class="letter"><svg width="8" height="4"><circle cx="2" cy="2" r="1.5" fill="none" stroke="#a5a5a7" stroke-width=".8"/><circle cx="6" cy="2" r="1.5" fill="none" stroke="#a5a5a7" stroke-width=".8"/></svg>V</div>
  <div class="entry"><h3>Versicherungsende</h3><p>Das Haustier ist solange versichert, wie der Halter die Prämien bezahlt und das Tier lebt.</p></div>
  <div class="entry"><h3>Versicherungssumme</h3><p>Dies ist der Höchstbetrag, den der Kunden von einem Versiche­rungsanbieter für eine Behandlung eines Haustieres erhält.</p></div>
  <div class="entry"><h3>Vertragsdauer</h3><p>Die Mindestlaufzeit von Tierversicherungen beträgt in der Regel ein Jahr.</p></div>
</section>

<aside class="fazit">
  <div class="fazit-ticks"></div>
  <h2>Fazit</h2>
  <p>Wir von der Felbor Tierärzte AG haben bisher sehr gute Erfahrungen mit Tierversicherungen unserer Kunden gemacht. Wir empfehlen Ihnen jedoch etwas Zeit in die Auswahl einer für sie passenden Tierversicherung zu investieren.</p>
</aside>
</body>
</html>
```